TolVeno is an ethnic owned company passionate about the CBD and cannabis industry.

*we are using amber colored bottles with white and gold lids*
Here are the dimensions of the bottles.
2 oz
4 ¼ inch Height
1 ¼ inch Diameter
4 inch Circumference
20/410 Neck Size

8 oz
186 mm Height
47 mm Diameter
24/410 Neck Size

On the front label we would like to add “Your wellness starts within”
Shampoo ingredients
Ingredients: Water Biotin Vitamin D3 (Cholecaliferol) Powder Decyl Glucoside Sulfosuccinate Coco Betaine Citric Acid Vegetable Glycerin Xanthan Gum Aloe Vera Pure Juice Horestail Extract Nettle Extract Saw Palmetto Extract Gingko Biloba Zinc PCA Honeyquat Peppermint EO Tea Tree EO Phenoxehtanol SA Vitamin B5 (D-Panthenol) CBD: Isolate MCT Oil Polysorbate 80

Shampoo How To Use: Apply a generous amount to the scalp and work toward the ends. Rinse thoroughly with cool water.
For best results, use in conjuction
with Tolveno CBD Conditioner.

Warning: For external use only, Avoid direct contact with eyes and mouth. Not intended for use by anyone under the age of 18 without adult supervision. Do not use if you are pregnant or nursing. Consult your physician prior to use if you are taking any medications. If any adverse reactions occur, discontinue use and consult your doctor.

This product contains a total delta-9-THC concentration that does not exceed 0.3% on a dry-weight basis. It is the customer’s responsibility to know applicable state and local laws in regard to use of this product.

*These statements have not been evaluated
by the Board of Tonic & Salve Review. This
product is not intended to diagnose, treat,
cure or prevent any disease.

TOLVENO COMPANY 412 ROUTE 57 #20318
TRENTON NJ 08791
TOLVENOCOMPANY.COM

*PLEASE ADD PROUDLY MADE IN THE USA SYMBOL AND RECYCLE SYMBOL*

Conditioner ingredients
Ingredients: Water Jojoba Oil Avocado Oil Grapeseed oil Argan Oil MCT Oil CBD: Isolate BTMS 50 Shea Butter Cetearyl Alchohol Lavender EO Peppermint EO Aloe Vera Pure Juice Honeyquat Phenoxehtanol SA Vitamin B5 (D-Panthenol)

Conditioner HOW TO USE: Apply to wet hair and gently lather with fingertips. Rinse and repeat. Leave on 5 minutes. For the best results.

WARNING: Consult your healthcare provider if you’re nursing, pregnant, or taking medication. If adverse reactions occur, discontinue use and consult your physician. Keep ou
t of the reach of children.

TRENTON NJ 08791
TOLVENOCOMPANY.COM

WE ALSO NEED A QR CODE PLACED ON THE BACK TO OUR SITE.

*PLEASE ADD PROUDLY MADE IN THE USA SYMBOL, RECYCLE SYMBOL, MINORITY OWNED BUSINESS*

Requirements
Must have
• *PLEASE USE COLOR PALETTE IN PHOTOS*
*We would like a black background for the label*
*The word CBD and the mg of CBD in each shampoo bottle size, 8 oz bottle 250 mg of CBD and 60 mg of CBD for the 2 oz bottle*
*We need two designs. One with set with CBD advertised on the bottles and one without for advertising and social media reasons!*
Should not have
• Cannabis leaves, the word hemp,

```html
<!DOCTYPE html>
<html lang="en">
<head>
<meta charset="utf-8">
<title>Tolveno CBD Shampoo – Wraparound Label</title>
<link rel="stylesheet" href="https://fonts.googleapis.com/css2?family=Raleway:wght@300;400;500&family=Open+Sans:wght@400;600;700&display=swap">
<style>
  :root {
    --backdrop: #ececec;
    --label: #141514;
    --sage: #7f9a8a;
    --sage-light: #9bb5a5;
    --ink: #d9dcda;
    --ink-soft: #c3c8c5;
    --rule: #7f8883;
    --mark: #c9cecb;
  }
  * { box-sizing: border-box; margin: 0; padding: 0; }
  html, body {
    width: 1200px; height: 1200px; overflow: hidden;
    background: var(--backdrop);
  }
  .label {
    position: absolute; left: 45px; top: 90px;
    width: 1110px; height: 1020px;
    background: var(--label);
    box-shadow: 0 2px 10px rgba(0,0,0,0.12);
  }
  .label__band {
    position: absolute; left: 0; width: 100%; height: 44px;
    background: var(--sage);
  }
  .label__band--top { top: 0; }
  .label__band--bottom { bottom: 0; }

  .panel {
    position: absolute; top: 44px; bottom: 44px; width: 370px;
    color: var(--ink);
    font-family: "Open Sans", sans-serif;
  }
  .panel--back { left: 0; }
  .panel--front { left: 370px; }
  .panel--side { left: 740px; }

  .copy { font-size: 13.5px; line-height: 1.42; color: var(--ink); }
  .copy strong { font-weight: 700; }
  .copy p + p { margin-top: 14px; }

  /* back panel */
  .panel--back .copy {
    position: absolute; left: 34px; top: 40px; width: 232px;
  }
  .company { font-size: 12.5px; line-height: 1.5; letter-spacing: 0.04em; }
  .qr-code {
    position: absolute; left: 34px; top: 560px;
    width: 110px; height: 110px;
    background: var(--ink);
    border: 8px solid var(--ink);
  }
  .product-name-vertical {
    position: absolute;
    font-family: "Raleway", sans-serif; font-weight: 500;
    color: var(--sage-light);
    writing-mode: vertical-rl;
    letter-spacing: 14px;
    font-size: 62px; line-height: 1;
  }
  .panel--back .product-name-vertical { right: 30px; top: 380px; }

  /* front panel */
  .panel--front .product-name-vertical {
    left: 30px; bottom: 40px;
    transform: rotate(180deg);
  }
  .brand {
    position: absolute; left: 120px; top: 52px; width: 220px;
    text-align: center; color: var(--sage-light);
    font-family: "Raleway", sans-serif;
  }
  .brand__dot {
    width: 58px; height: 58px; border-radius: 50%;
    background: var(--sage); margin: 0 auto 10px;
  }
  .brand__name { font-size: 26px; font-weight: 500; letter-spacing: 0.22em; }
  .claim {
    position: absolute; left: 120px; top: 190px; width: 230px;
    font-family: "Raleway", sans-serif; color: var(--ink-soft);
  }
  .claim__cbd { font-size: 120px; font-weight: 300; line-height: 1; letter-spacing: 0.02em; }
  .claim__sub { font-size: 34px; font-weight: 300; letter-spacing: 0.08em; margin-top: 4px; }
  .tagline {
    position: absolute; left: 120px; top: 395px; width: 220px;
    border-top: 1.5px solid var(--rule); border-bottom: 1.5px solid var(--rule);
    padding: 18px 0;
    font-family: "Raleway", sans-serif; font-weight: 500;
    font-size: 20px; line-height: 1.35; letter-spacing: 0.14em;
    color: var(--ink-soft);
  }
  .volume {
    position: absolute; left: 120px; top: 600px;
    font-family: "Raleway", sans-serif; color: var(--ink-soft);
    display: flex; align-items: center; gap: 10px;
  }
  .volume__num { font-size: 110px; font-weight: 300; line-height: 1; }
  .volume__unit { font-size: 20px; line-height: 1.35; letter-spacing: 0.08em; }

  /* side panel */
  .panel--side .copy { position: absolute; left: 36px; top: 40px; width: 298px; }
  .marks {
    position: absolute; left: 36px; bottom: 60px;
    display: flex; gap: 22px; align-items: center;
  }
</style>
</head>
<body>
  <div class="label">
    <div class="label__band label__band--top"></div>
    <div class="label__band label__band--bottom"></div>

    <section class="panel panel--back">
      <div class="copy">
        <p><strong>Ingredients:</strong> Water Biotin Vitamin D3 (Cholecaliferol) Powder Decyl Glucoside Sulfosuccinate Coco Betaine Citric Acid Vegetable Glycerin Xanthan Gum Aloe Vera Pure Juice Horestail Extract Nettle Extract Saw Palmetto Extract Gingko Biloba Zinc PCA Honeyquat Peppermint EO Tea Tree EO Phenoxehtanol SA Vitamin B5 (D-Panthenol) CBD: Isolate MCT Oil Polysorbate 80</p>
        <p><strong>How To Use:</strong> Apply a generous amount to the scalp and work toward the ends. Rinse thoroughly with cool water.</p>
        <p>For best results, use in conjuction with Tolveno CBD Conditioner.</p>
        <p class="company">TOLVENO COMPANY<br>412 ROUTE 57 #20318<br>TRENTON NJ 08791<br>TOLVENOCOMPANY.COM</p>
      </div>
      <div class="qr-code" role="img" aria-label="QR code linking to the company website"></div>
      <div class="product-name-vertical">SHAMPOO</div>
    </section>

    <section class="panel panel--front">
      <div class="product-name-vertical">SHAMPOO</div>
      <div class="brand">
        <div class="brand__dot"></div>
        <div class="brand__name">TOLVENO</div>
      </div>
      <div class="claim">
        <div class="claim__cbd">CBD</div>
        <div class="claim__sub">250 MG</div>
      </div>
      <div class="tagline">YOUR<br>WELLNESS<br>STARTS<br>WITHIN</div>
      <div class="volume">
        <span class="volume__num">8</span>
        <span class="volume__unit">FL OZ<br>/ 237 ML</span>
      </div>
    </section>

    <section class="panel panel--side">
      <div class="copy">
        <p><strong>Warning:</strong> For external use only. Avoid direct contact with eyes and mouth. Not intended for use by anyone under the age of 18 without adult supervision. Do not use if you are pregnant or nursing. Consult your physician prior to use if you are taking any medications. If any adverse reactions occur, discontinue use and consult your doctor.</p>
        <p>This product contains a total delta-9-THC concentration that does not exceed 0.3% on a dry-weight basis. It is the customer’s responsibility to know applicable state and local laws in regard to use of this product.</p>
        <p>*These statements have not been evaluated by the Board of Tonic &amp; Salve Review. This product is not intended to diagnose, treat, cure or prevent any disease.</p>
      </div>
      <div class="marks">
        <svg width="62" height="62" viewBox="0 0 62 62" role="img" aria-label="Recycle mark">
          <circle cx="31" cy="31" r="29" fill="none" stroke="var(--mark)" stroke-width="3"/>
          <path d="M31 17 L42 36 L20 36 Z" fill="none" stroke="var(--mark)" stroke-width="3" stroke-linejoin="round"/>
        </svg>
        <svg width="62" height="62" viewBox="0 0 62 62" role="img" aria-label="Packaging mark">
          <circle cx="31" cy="31" r="29" fill="none" stroke="var(--mark)" stroke-width="3"/>
          <circle cx="31" cy="31" r="15" fill="var(--mark)"/>
        </svg>
        <svg width="62" height="62" viewBox="0 0 62 62" role="img" aria-label="Made in the USA badge">
          <rect x="4" y="8" width="54" height="46" rx="4" fill="var(--mark)"/>
        </svg>
      </div>
    </section>
  </div>
</body>
</html>
```